Local Roofing/Construction company business needs new biz card design

We need a new business card design, current cards are from the start of this operation and generic at best. We are a local Construction Company (General Contractor) with a majority of our work originating from insurance claims-exterior finish work is the main focus (Roofs-Siding-Gutters etc). Heavily involved with homeowners and the low ball offers they receive from insurance company's after a insurable event takes place. I have attached some of our original logo file(s) below.

```html
<!DOCTYPE html>
<html lang="en">
<head>
<meta charset="utf-8">
<title>Ridgeline Build Co. – Business Card</title>
<link href="https://fonts.googleapis.com/css2?family=Montserrat:wght@400;500;700;800&display=swap" rel="stylesheet">
<style>
  :root{
    --green:#4cb86a;
    --green-dark:#3fa35c;
    --ink:#1f1f1f;
    --paper:#f8f6f3;
    --muted:#d9dbda;
    --stage:#2a2b2e;
  }
  *{margin:0;padding:0;box-sizing:border-box}
  html,body{width:1200px;height:900px;overflow:hidden}
  body{background:var(--stage);font-family:'Montserrat',sans-serif;position:relative}
  .card{position:absolute;left:240px;width:720px;height:411px;border-radius:26px;overflow:hidden}
  .card--front{top:26px;background:var(--green)}
  .card--back{top:463px;background:var(--paper);color:var(--ink)}

  .front-pattern{position:absolute;inset:0;background:linear-gradient(135deg,var(--green) 0%,var(--green-dark) 100%)}
  .front-mark{position:absolute;right:40px;top:40px;display:flex;align-items:center;gap:8px;color:#fff;font-weight:800;font-size:15px;letter-spacing:.5px}
  .front-mark .square{width:18px;height:18px;background:#fff;border-radius:3px}

  .brand{position:absolute;left:40px;top:46px;display:flex;align-items:center;gap:12px}
  .brand .square{width:34px;height:34px;background:var(--green);border-radius:4px}
  .brand .name{font-weight:800;font-size:30px;letter-spacing:1px;color:var(--ink)}

  .ghost-mark{position:absolute;right:70px;top:50px;font-weight:800;font-size:36px;color:var(--muted);text-align:right;line-height:1}

  .person{position:absolute;left:60px;top:148px}
  .person .full-name{font-weight:700;font-size:30px;color:var(--green)}
  .person .role{font-weight:500;font-size:17px;margin-top:2px}
  .rule{position:absolute;left:60px;right:60px;top:214px;height:1.5px;background:var(--green)}

  .contacts{position:absolute;left:72px;top:228px;list-style:none;font-size:17px;line-height:27px}
  .contacts li{display:flex;align-items:center;gap:14px}
  .contacts svg{width:16px;height:16px;fill:var(--green)}

  .address{position:absolute;right:60px;top:246px;text-align:right;font-size:17px;line-height:25px;font-weight:500}

  .footer{position:absolute;left:0;bottom:0;width:720px;height:100px}
  .footer .web{position:absolute;right:24px;bottom:52px;color:#fff;font-size:15px;font-weight:500}
</style>
</head>
<body>
  <section class="card card--front">
    <div class="front-pattern" role="img" aria-label="Repeating tone-on-tone brand pattern across the green card face"></div>
    <div class="front-mark"><span class="square"></span><span>RIDGELINE BUILD</span></div>
  </section>

  <section class="card card--back">
    <div class="brand"><span class="square"></span><span class="name">RIDGELINE BUILD</span></div>
    <div class="ghost-mark">RIDGELINE<br>BUILD CO.</div>

    <div class="person">
      <div class="full-name">Jonah Whitcombe</div>
      <div class="role">Managing Director</div>
    </div>
    <div class="rule"></div>

    <ul class="contacts">
      <li><svg viewBox="0 0 16 16"><path d="M3 1l3 3-2 2c1 2 3 4 5 5l2-2 3 3-2 3C6 14 2 10 1 4z"/></svg>555-201-3380</li>
      <li><svg viewBox="0 0 16 16"><path d="M4 0h8a1 1 0 011 1v14a1 1 0 01-1 1H4a1 1 0 01-1-1V1a1 1 0 011-1zm1 2v10h6V2z"/></svg>555-201-3380</li>
      <li><svg viewBox="0 0 16 16"><path d="M0 3h16v10H0zm1 1v1l7 4 7-4V4z"/></svg>info@ridgelinebuild.com</li>
      <li><svg viewBox="0 0 16 16"><circle cx="8" cy="8" r="7" fill="none" stroke="#4cb86a" stroke-width="2"/><path d="M1 8h14M8 1c3 3 3 11 0 14M8 1c-3 3-3 11 0 14" fill="none" stroke="#4cb86a" stroke-width="1.3"/></svg>www.ridgelinebuild.com</li>
    </ul>

    <div class="address">418 Maple Row, Suite 12<br>Fairhaven, OH 43010</div>

    <div class="footer">
      <svg width="720" height="100" viewBox="0 0 720 100">
        <polygon points="452,20 720,20 720,60 452,60 440,40" fill="#4cb86a"/>
        <polygon points="0,80 440,40 452,40 452,60 0,95" fill="#1f1f1f"/>
        <polygon points="0,95 452,60 720,60 720,100 0,100" fill="#4cb86a"/>
      </svg>
      <div class="web">www.ridgelinebuild.com</div>
    </div>
  </section>
</body>
</html>
```